Civil Engineering Business Card Design

We need a business card design for an Civil Engineering Company located in Naples, Florida. The company name is Dorvel Engineering.
What we do:
Site Evaluation
Review existing site conditions and zoning
Evaluation of potential development options
Evaluation of environmental permitting challenges
Prepare alternative master site development or redevelopment plan
Calculate cost and time lines for site development
Address political, environmental, social, and economic impacts of site development
Site Design
Prepare master site development plans
Zoning, rezoning, and zoning amendments for land use changes
Evaluate zoning and environmental permitting challenges
Value engineer alternative land development design and products
Residential Development
Plat development and design
Homeowner association document development
Single family development ranging from affordable housing to large estate projects
Multi family development ranging from duplexes to large scale condominiums
Amenity facilities such as golf courses, parks and clubhouse sites
Commercial Development
Office site and park designs development plans
Industrial site and park development plans
Shopping center site development design
Hospital site design development
Institutional Development
School design development and redevelopment plans
Park design development and enhancement plans
Downtown redevelopment plans for new and existing structures
Theater and park plan development
Parking garage design development
Governmental administration building design
Design Services
Site development
Environmental assessment
Roadway alignment and development
Surface water management
Drainage design
Water distribution system
Fire service analysis
Sewage collection systems
Sewage pump station and force main design
Cable utility conduit layout
Construction details
Construction documents
Technical specifications
Alternative methods and materials analysis
Services During Construction
Development of bid documents
Solicitation and processing of bids
Cost review and analysis
Construction cost estimating
Onsite construction observation
Coordination of field modifications to address unforeseen site conditions
Assess value engineering design and contract work
Review of pay requests and shop drawings
Review of warranties
Development assessment of onsite and offsite mitigation
Verification of construction completion, close out, and certification
Processing final pay requests and turn over
We want a clean design on a white background. We have a current logo but are not happy with it so changes would be greatly appreciated.
Industry/Entity Type
Construction
Contact Information for Business Card
Dorvel Engineering
Sound Site Design Shaped by Careful Planning and Lasting Craft
Marcus Dorvel, President
4817 Bracken Loop West
Suite 418C
Naples, FL 34987
239-555-0143-Office, 239-555-0178-Mobile
Marc@DorvelEng.com, www.DorvelEng.com

```html
<!DOCTYPE html>
<html lang="en">
<head>
<meta charset="utf-8">
<title>Dorvel Engineering – Business Card</title>
<link href="https://fonts.googleapis.com/css2?family=Montserrat:wght@600;700&family=Quicksand:wght@400;500&display=swap" rel="stylesheet">
<style>
  :root {
    --backdrop: #e4e5e7;
    --card: #ffffff;
    --brand-blue: #0b6fc1;
    --ink: #2f2f33;
    --ink-soft: #55575c;
    --on-blue: #ffffff;
  }
  html, body {
    margin: 0;
    width: 1200px;
    height: 1000px;
    overflow: hidden;
    background: var(--backdrop);
  }
  .business-card {
    position: absolute;
    left: 180px;
    top: 260px;
    width: 840px;
    height: 480px;
    background: var(--card);
    box-shadow: 0 10px 30px rgba(0,0,0,0.12);
    font-family: "Quicksand", sans-serif;
    color: var(--ink-soft);
  }
  .brand {
    position: absolute;
    left: 44px;
    top: 48px;
    display: flex;
    align-items: center;
    gap: 12px;
  }
  .brand-square {
    width: 22px;
    height: 22px;
    background: var(--brand-blue);
  }
  .brand-name {
    font-family: "Montserrat", sans-serif;
    font-weight: 700;
    font-size: 24px;
    letter-spacing: 0.5px;
    color: var(--ink);
  }
  .person {
    position: absolute;
    right: 40px;
    top: 100px;
    padding-right: 14px;
    border-right: 8px solid var(--brand-blue);
    text-align: right;
  }
  .person-name {
    font-family: "Montserrat", sans-serif;
    font-weight: 700;
    font-size: 23px;
    letter-spacing: 1px;
    color: var(--brand-blue);
    margin: 0;
  }
  .person-title {
    font-size: 21px;
    font-weight: 500;
    color: var(--ink);
    margin: 2px 0 0;
  }
  .contact-list {
    position: absolute;
    left: 44px;
    top: 150px;
    margin: 0;
    padding: 0;
    list-style: none;
  }
  .contact-item {
    display: flex;
    align-items: center;
    gap: 16px;
    height: 38px;
    font-size: 23px;
    font-weight: 500;
  }
  .contact-icon {
    width: 18px;
    height: 18px;
    fill: var(--brand-blue);
    flex: none;
  }
  .office {
    position: absolute;
    right: 40px;
    top: 290px;
    text-align: left;
  }
  .office-name {
    font-family: "Montserrat", sans-serif;
    font-weight: 600;
    font-size: 22px;
    color: var(--ink);
    margin: 0 0 2px;
  }
  .office-address {
    font-size: 21px;
    font-weight: 500;
    line-height: 1.3;
    margin: 0;
    font-style: normal;
  }
  .tagline-band {
    position: absolute;
    left: 0;
    top: 398px;
    width: 790px;
    height: 50px;
    background: var(--brand-blue);
    display: flex;
    align-items: center;
    padding-left: 44px;
    box-sizing: border-box;
  }
  .tagline {
    color: var(--on-blue);
    font-size: 24px;
    font-weight: 400;
    letter-spacing: 0.3px;
    margin: 0;
    white-space: nowrap;
  }
</style>
</head>
<body>
  <div class="business-card">
    <div class="brand">
      <span class="brand-square"></span>
      <span class="brand-name">DORVEL ENGINEERING</span>
    </div>

    <div class="person">
      <p class="person-name">MARCUS DORVEL</p>
      <p class="person-title">President</p>
    </div>

    <ul class="contact-list">
      <li class="contact-item">
        <svg class="contact-icon" viewBox="0 0 24 24" aria-hidden="true"><path d="M6.6 10.8a15.1 15.1 0 0 0 6.6 6.6l2.2-2.2c.3-.3.7-.4 1-.2 1.1.4 2.3.6 3.6.6.6 0 1 .4 1 1V20c0 .6-.4 1-1 1A17 17 0 0 1 3 4c0-.6.4-1 1-1h3.5c.6 0 1 .4 1 1 0 1.3.2 2.5.6 3.6.1.3 0 .7-.2 1z"/></svg>
        <span>239-555-0143</span>
      </li>
      <li class="contact-item">
        <svg class="contact-icon" viewBox="0 0 24 24" aria-hidden="true"><path d="M7 1h10a2 2 0 0 1 2 2v18a2 2 0 0 1-2 2H7a2 2 0 0 1-2-2V3a2 2 0 0 1 2-2zm0 3v14h10V4zm5 15.5a1 1 0 1 0 0 2 1 1 0 0 0 0-2z"/></svg>
        <span>239-555-0178</span>
      </li>
      <li class="contact-item">
        <svg class="contact-icon" viewBox="0 0 24 24" aria-hidden="true"><path d="M12 2a10 10 0 1 0 0 20 10 10 0 0 0 0-20zm6.9 6h-3a15.7 15.7 0 0 0-1.4-3.6A8 8 0 0 1 18.9 8zM12 4c.8 1.2 1.5 2.5 1.9 4h-3.8c.4-1.5 1.1-2.8 1.9-4zM4.3 14a8 8 0 0 1 0-4h3.4a16.5 16.5 0 0 0 0 4zm.8 2h3a15.7 15.7 0 0 0 1.4 3.6A8 8 0 0 1 5.1 16zm3-8h-3a8 8 0 0 1 4.4-3.6C8.9 5.6 8.4 6.8 8.1 8zM12 20c-.8-1.2-1.5-2.5-1.9-4h3.8c-.4 1.5-1.1 2.8-1.9 4zm2.3-6H9.7a14.7 14.7 0 0 1 0-4h4.6a14.7 14.7 0 0 1 0 4zm.2 5.6c.6-1.1 1.1-2.3 1.4-3.6h3a8 8 0 0 1-4.4 3.6zm1.8-5.6a16.5 16.5 0 0 0 0-4h3.4a8 8 0 0 1 0 4z"/></svg>
        <span>www.DorvelEng.com</span>
      </li>
      <li class="contact-item">
        <svg class="contact-icon" viewBox="0 0 24 24" aria-hidden="true"><path d="M2 5h20v14H2zm2 2v.5l8 5 8-5V7zm0 2.8V17h16V9.8l-8 5z"/></svg>
        <span>Marc@DorvelEng.com</span>
      </li>
    </ul>

    <div class="office">
      <p class="office-name">Dorvel Engineering</p>
      <address class="office-address">4817 Bracken Loop West,<br>Suite 418C, Naples, FL 34987</address>
    </div>

    <div class="tagline-band">
      <p class="tagline">Sound Site Design Shaped by Careful Planning and Lasting Craft</p>
    </div>
  </div>
</body>
</html>
```